Spiritual Self Help Book Cover

I need a book cover that's extremely appealing to spiritual seekers, self-help/health and wellness fans. Mostly for women.
The book blends spirituality/mysticism with science for readers to understand how to optimize their health/body, emotional well-being, mental wellness, spiritual fulfillment, relationships, business and purpose in life. It infuses ancient and modern understanding of energy/frequency/quantum mechanics along with the science of chiropractic and psychology.
Book title: Folding Every Lantern Inward
I'll attach some examples that are similar to what I like but I want something different and more extravagantly beautiful.
Please use the graphic of the Sri Yantra Mandala into the cover instead of this stock image one.
I'll need the book cover in all formats: paperback, hardcover, ebook and audiobook.
I'll provide the rest of the details, including publisher logo, synopsis, author photo/blurb and ISBN after I pick the final wniner.
Mostly women spiritual seekers, self-help readers, health/wellness enthusiasts

```html
<!DOCTYPE html>
<html lang="en">
<head>
<meta charset="UTF-8">
<title>Folding Every Lantern Inward — Book Cover</title>
<link href="https://fonts.googleapis.com/css2?family=Amatic+SC:wght@400;700&family=Oswald:wght@500;600&display=swap" rel="stylesheet">
<style>
  :root {
    --backdrop: #2b2b2c;
    --cover-red-light: #c0474a;
    --cover-red: #b3302f;
    --cover-red-deep: #a11f24;
    --title-cream: #e4d3a2;
    --title-white: #f3efe6;
    --line-white: #f1ece6;
    --author-white: #f7f3ee;
  }
  * { margin: 0; padding: 0; box-sizing: border-box; }
  html, body {
    width: 1200px;
    height: 900px;
    overflow: hidden;
    background: var(--backdrop);
  }
  .canvas {
    position: relative;
    width: 1200px;
    height: 900px;
    display: flex;
    align-items: center;
    justify-content: center;
  }
  .book-cover {
    position: relative;
    width: 584px;
    height: 820px;
    background: linear-gradient(135deg, var(--cover-red-light) 0%, var(--cover-red) 45%, var(--cover-red-deep) 100%);
  }
  .yantra-emblem {
    position: absolute;
    left: 155px;
    top: 96px;
    width: 274px;
    height: 274px;
  }
  .book-title {
    position: absolute;
    left: 0;
    right: 0;
    top: 430px;
    text-align: center;
    font-family: "Amatic SC", cursive;
    font-weight: 400;
    line-height: 0.92;
    text-transform: uppercase;
    background: linear-gradient(90deg, var(--title-cream) 20%, var(--title-white) 80%);
    -webkit-background-clip: text;
    background-clip: text;
    color: transparent;
  }
  .book-title span { display: block; }
  .title-line-top { font-size: 84px; letter-spacing: 1px; }
  .title-line-main { font-size: 132px; letter-spacing: 2px; }
  .title-line-end { font-size: 54px; letter-spacing: 1px; margin-top: 2px; }
  .author-name {
    position: absolute;
    left: 0;
    right: 0;
    top: 756px;
    text-align: center;
    font-family: "Oswald", sans-serif;
    font-weight: 600;
    font-size: 21px;
    letter-spacing: 0.3px;
    color: var(--author-white);
    text-transform: uppercase;
  }
</style>
</head>
<body>
  <main class="canvas">
    <section class="book-cover">
      <svg class="yantra-emblem" viewBox="0 0 274 274" role="img" aria-label="Line-drawn yantra mandala emblem: square gated frame with lotus petals around a nested downward triangle">
        <defs>
          <radialGradient id="emblemGlow" cx="50%" cy="50%" r="50%">
            <stop offset="0%" stop-color="#f1ece6" stop-opacity="0.22"/>
            <stop offset="100%" stop-color="#f1ece6" stop-opacity="0.06"/>
          </radialGradient>
        </defs>
        <rect x="0" y="0" width="274" height="274" fill="url(#emblemGlow)"/>
      </svg>

      <h1 class="book-title">
        <span class="title-line-top">Folding Every</span>
        <span class="title-line-main">Lantern</span>
        <span class="title-line-end">Inward</span>
      </h1>

      <p class="author-name">Dr. Lydia Harrowgate</p>
    </section>
  </main>
</body>
</html>
```